Harborline Talent IT Recruiting firm needs a business card design for Recruiters, Sourcers, and Account

We need business cards that allow us to change all contact info, names, titles (Recruiter, Sourcer, Account Manager, Director, CEO, etc) per person since we have three offices, in three cities, Phoenix, Austin, and Las Vegas. We do recruiting and contractors for IT positions (Developers, Architects, Software Engineers, Security Engineers, Help Desk, DBAs, PMs, Scrum Masters, etc.) Our client companies are very diverse from Crestline 250 to silicone Valley type start-ups.

So, while we what hip, techie, and quirky, it still needs to be professional. Primary color we use is blue, with silver as a secondary color.

Target Market(s)

IT, Technology

Industry/Entity Type

Business

Contact Information for Business Card

Company name: Harborline Talent, Inc.
Website: www.harborlinetalent-example.com
Logos for ProCircle, Quillo, and Roomwall

Name, Title, Office Number, Cell Number, email

Font styles to use
Serif
Sans Serif

Colors
0455a3
d5d5d5

Requirements
Nice to have
• The grey I selected below is not necessary - but, would like silver included. I included a card design (File 3: HTI early trial example.jpg) that I had started on. It's very rough, and not quite what we're looking for, but what we did like is the logo, big, maybe a bit faded, off center, goes out of frame, etc. Still looking for other ideas - you are the pros! But, just an idea of a design element we liked.

```html
<!DOCTYPE html>
<html lang="en">
<head>
<meta charset="utf-8">
<title>Harborline Talent – Business Card</title>
<link rel="stylesheet" href="https://fonts.googleapis.com/css2?family=Tenor+Sans&family=Marcellus&display=swap">
<style>
  :root {
    --blue: #0455a3;
    --blue-deep: #1d44a0;
    --blue-bright: #1f9be0;
    --silver: #d5d5d5;
    --ink: #1b1f2a;
    --white: #ffffff;
    --backdrop: #2a2b2e;
  }
  * { box-sizing: border-box; margin: 0; padding: 0; }
  html, body {
    width: 1200px; height: 900px; overflow: hidden;
    background: var(--backdrop);
  }
  .canvas { position: relative; width: 1200px; height: 900px; }

  .card {
    position: absolute; width: 700px; height: 400px;
    border-radius: 22px; overflow: hidden;
    box-shadow: 0 18px 40px rgba(0,0,0,.45);
  }

  /* Back side */
  .card-back { left: 70px; top: 50px; background: var(--white); }
  .card-back .emblem-area {
    position: absolute; left: 60px; top: -40px; width: 440px; height: 460px;
    border-radius: 50%;
    background: radial-gradient(circle at 50% 35%, var(--blue-bright), var(--blue) 85%);
  }
  .card-back .brand {
    position: absolute; left: 60px; width: 440px; top: 228px; text-align: center;
    font-family: "Tenor Sans", sans-serif; color: var(--white);
  }
  .card-back .brand-name { font-size: 32px; letter-spacing: 1px; white-space: nowrap; }
  .card-back .brand-tagline {
    font-family: "Marcellus", serif; font-size: 16px; letter-spacing: 2px;
    margin-top: 6px; text-transform: uppercase; white-space: nowrap;
  }
  .social-row { display: flex; gap: 8px; justify-content: center; margin-top: 12px; }
  .social-row span { width: 16px; height: 16px; border-radius: 3px; background: var(--white); }

  /* Front side */
  .card-front { left: 430px; top: 450px; background: linear-gradient(160deg, var(--blue-deep), var(--blue)); }
  .card-front .art { position: absolute; inset: 0; }
  .contact {
    position: absolute; left: 44px; top: 52px; color: var(--white);
    font-family: "Tenor Sans", sans-serif;
  }
  .person-name { font-size: 24px; line-height: 1.2; }
  .person-title { font-size: 11px; letter-spacing: 1px; text-transform: uppercase; margin-top: 2px; }
  .office { font-size: 15px; line-height: 1.35; margin-top: 20px; }
  .website { font-weight: 700; }
  .lines { margin-top: 16px; font-size: 15px; line-height: 1.6; }
  .lines li { list-style: none; display: flex; align-items: center; gap: 10px; white-space: nowrap; }
  .lines svg { width: 15px; height: 15px; flex: none; }
  .logo-lockup {
    position: absolute; right: 26px; top: 208px; display: flex; align-items: center; gap: 10px;
    font-family: "Tenor Sans", sans-serif; font-size: 20px; color: var(--ink);
    letter-spacing: 1px; white-space: nowrap;
  }
  .logo-lockup .dot { width: 24px; height: 24px; border-radius: 50%; background: var(--blue); }
  .tagline {
    position: absolute; left: 0; right: 0; bottom: 20px; text-align: center;
    font-family: "Marcellus", serif; font-size: 24px; letter-spacing: 8px;
    color: var(--silver); text-transform: uppercase; white-space: nowrap;
  }
</style>
</head>
<body>
<main class="canvas">

  <section class="card card-back" aria-label="Card back">
    <div class="emblem-area" role="img" aria-label="Large blue company emblem, bleeding off the top of the card"></div>
    <div class="brand">
      <div class="brand-name">HARBORLINE TALENT</div>
      <div class="brand-tagline">Built for What Comes Next</div>
      <div class="social-row" aria-label="Social profiles: ProCircle, Quillo, Roomwall">
        <span></span><span></span><span></span>
      </div>
    </div>
  </section>

  <section class="card card-front" aria-label="Card front">
    <svg class="art" viewBox="0 0 700 400" width="700" height="400">
      <defs>
        <linearGradient id="emblem-fade" x1="0" y1="0" x2="1" y2="1">
          <stop offset="0" stop-color="#ffffff"/>
          <stop offset="1" stop-color="#d5d5d5"/>
        </linearGradient>
      </defs>
      <path role="img" aria-label="Oversized silver company emblem, off centre and cropped by the card edge"
            d="M420 0 H700 V262 Q580 322 460 328 Q410 190 420 0 Z" fill="url(#emblem-fade)"/>
    </svg>

    <div class="contact">
      <div class="person-name">Daniel Marrow</div>
      <div class="person-title">Managing Director</div>
      <div class="office">
        PHOENIX OFFICE<br>
        4210 E Cantera Way, Suite 310<br>
        Phoenix, AZ 85099, USA<br>
        <span class="website">www.harborlinetalent-example.com</span>
      </div>
      <ul class="lines">
        <li>
          <svg viewBox="0 0 16 16" aria-hidden="true"><path d="M2 6c0-2 2-3 6-3s6 1 6 3l-2 1-1-2H5L4 7 2 6Zm2 2h8l1 5H3l1-5Zm4 1.2a1.8 1.8 0 1 0 0 3.6 1.8 1.8 0 0 0 0-3.6Z" fill="#fff"/></svg>
          480 555 01 42
        </li>
        <li>
          <svg viewBox="0 0 16 16" aria-hidden="true"><rect x="4.5" y="1.5" width="7" height="13" rx="1.5" fill="none" stroke="#fff" stroke-width="1.4"/><circle cx="8" cy="12.2" r=".9" fill="#fff"/></svg>
          602 555 01 87
        </li>
        <li>
          <svg viewBox="0 0 16 16" aria-hidden="true"><rect x="1.5" y="3.5" width="13" height="9" fill="#fff"/><path d="M1.5 3.5 8 9l6.5-5.5" fill="none" stroke="#1d44a0" stroke-width="1.2"/></svg>
          dmarrow@harborlinetalent-example.com
        </li>
      </ul>
    </div>

    <div class="logo-lockup"><span class="dot"></span>HARBORLINE TALENT</div>
    <div class="tagline">Built for What Comes Next</div>
  </section>

</main>
</body>
</html>
```